Web Design Project

We are looking for a new site design for the VELTO Canada. The current site can be found at
http://www.veltocanada-example.org/
The URL is provided for reference. We want a completely different look and layout which is shown in the specifications document.
As part of the design, we want a home page, and inside page.
The design you provide will be implemented in Joomla. The design winner will only need to provide the PSD. We anticipate creating the template coding in-house.
However, if you have experience creating Joomla templates, please let us know as we may ask you to bid separately to do that phase of the project.
We've provided a specifications document which includes wireframes of the home page, and inside page. We've also included a logo file.
For the header at the top, as indicated in the specs document, we want to keep the same overall treatment to every page. We want a graphic treatment with the logo for the header area. In this manner, the design will be flexiable and can be used for future years.
For the home page, we've indicated that we'd like to have a slider implemented within the design.
The wireframe is provided to illustrate the placement of content and menu items. The exact dimensions of each component can be revised as you see fit. We are also flexiable if you feel we have missed items.

```html
<!DOCTYPE html>
<html lang="en">
<head>
<meta charset="utf-8">
<title>VELTO Canada Conference</title>
<link href="https://fonts.googleapis.com/css2?family=Arimo:wght@400;700&family=Open+Sans:wght@400;600;700&display=swap" rel="stylesheet">
<style>
:root{
  --page-bg:#f1f1f1;
  --white:#ffffff;
  --panel:#ededed;
  --panel-border:#d6d6d6;
  --blue:#2f4b8f;
  --blue-light:#4262ab;
  --blue-dark:#233a74;
  --red:#e3332f;
  --red-text:#d11f1f;
  --text:#222222;
  --muted:#555555;
  --footer:#444444;
}
*{box-sizing:border-box;margin:0;padding:0}
html,body{width:1200px;height:1197px;overflow:hidden}
body{background:var(--page-bg);font-family:"Arimo",Arial,sans-serif;color:var(--text);position:relative}
a{color:inherit;text-decoration:none}
ul{list-style:none}

.page{position:absolute;left:113px;top:18px;width:974px;height:1111px;background:var(--white);box-shadow:0 0 4px rgba(0,0,0,.18)}
.header{position:absolute;left:3px;top:3px;width:968px;height:169px;background:linear-gradient(#f0f0f0,#fafafa 60%,#f2f2f2)}
.brand{position:absolute;left:18px;top:22px;display:flex;align-items:center;gap:12px}
.brand-dot{width:22px;height:22px;border-radius:50%;background:var(--red)}
.brand-name{font-family:"Open Sans",sans-serif;font-weight:700;font-size:30px;color:var(--blue);line-height:1}
.top-links{position:absolute;right:13px;top:18px;font-size:12px;color:var(--text);display:flex;gap:17px}
.social-top{position:absolute;right:14px;top:128px;display:flex;gap:11px}
.social-top span{width:28px;height:28px;background:var(--blue-light);display:block}

.nav{position:absolute;left:0;top:172px;width:974px;height:42px;background:linear-gradient(var(--blue-light),var(--blue-dark));display:flex;padding-left:10px}
.nav a{color:var(--white);font-size:14px;line-height:42px;text-align:center;border-right:1px solid rgba(255,255,255,.18)}
.nav a:last-child{border-right:none}
.nav a.active{background:var(--red)}

.banner{position:absolute;left:31px;top:234px;width:925px;height:295px;background:linear-gradient(#c9d1dc 0%,#d9cfc2 25%,#8a8f6c 45%,#6f7c74 62%,#4f5a38 100%)}

.box{position:absolute;background:var(--panel);border:1px solid var(--panel-border)}
.box h2{font-family:"Open Sans",sans-serif;font-weight:600;font-size:19px;color:#333;margin:6px 10px 0 11px;padding-bottom:3px;border-bottom:1px solid #cfcfcf}
.sponsors{left:7px;top:562px;width:231px;height:207px}
.badge{position:absolute;border-radius:8px}
.login{left:8px;top:786px;width:230px;height:169px}
.field{position:absolute;left:8px;width:214px;height:32px;border-radius:16px;background:var(--white);border:1px solid #d2d2d2;box-shadow:inset 0 2px 3px rgba(0,0,0,.08);font-size:12px;color:#888;padding:10px 12px}
.login-btn{position:absolute;left:140px;top:134px;width:80px;height:26px;border-radius:13px;background:linear-gradient(#d34a3c,#a92a20);color:var(--white);font-family:"Open Sans",sans-serif;font-weight:700;font-size:13px;text-align:center;line-height:26px}
.connect{left:7px;top:975px;width:231px;height:96px}
.connect-icons{position:absolute;left:41px;top:48px;display:flex;gap:13px}
.connect-icons span{width:27px;height:27px;border-radius:3px;background:var(--blue-light);display:block}

.welcome{position:absolute;left:257px;top:565px;width:435px}
.welcome h1{font-family:"Open Sans",sans-serif;font-weight:600;font-size:21px;color:#333}
.welcome h1 em{font-style:normal;color:var(--blue)}
.welcome p{font-size:12px;line-height:18px;text-align:justify;margin-top:14px}
.welcome p + p{margin-top:18px}

.news{left:730px;top:562px;width:233px;height:267px;background:linear-gradient(#ededed,#fdfdfd);border-color:#e6e6e6}
.news h2{font-family:"Arimo",sans-serif;font-weight:400;font-size:18px;border:none;margin:10px 0 0 16px;color:#333}
.news h2 em{font-style:normal;color:var(--red-text)}
.news ul{margin:16px 14px 0 16px}
.news li{position:relative;padding-left:14px;font-size:12.5px;line-height:18px;margin-bottom:18px}
.news li::before,.regions li::before{content:"";position:absolute;left:0;top:5px;border-left:4px solid var(--red-text);border-top:4px solid transparent;border-bottom:4px solid transparent}
.news strong{color:#333}
.news .desc{color:#444}
.news time{display:block;color:var(--red-text);font-size:11px}

.regions{left:252px;top:894px;width:716px;height:197px;background:linear-gradient(#e9e9e9,#fbfbfb);border-color:#ececec}
.regions h2{font-family:"Open Sans",sans-serif;font-weight:600;font-size:23px;border:none;margin:14px 0 0 21px;color:#222}
.region{position:absolute;top:60px}
.region h3{font-family:"Open Sans",sans-serif;font-weight:700;font-size:14px;color:var(--red-text)}
.region ul{margin-top:13px}
.regions li{position:relative;padding-left:16px;font-size:12.5px;line-height:24px}
.regions li::before{top:8px}

.footer{position:absolute;left:0;top:1129px;width:1200px;height:68px;background:var(--footer);color:var(--white);font-size:12.5px;text-align:center}
.footer p{line-height:24px}
.footer p:first-child{margin-top:9px;padding-left:0;margin-left:-38px}
.footer p:last-child{margin-left:-10px}
.sep{margin:0 9px}
</style>
</head>
<body>
<div class="page">
  <header class="header">
    <div class="brand"><span class="brand-dot"></span><span class="brand-name">VELTO Canada</span></div>
    <nav class="top-links"><a href="#">Home</a><span>|</span><a href="#">Contact Us</a><span>|</span><a href="#">VELTO International</a></nav>
    <div class="social-top" aria-label="Social links"><span></span><span></span><span></span><span></span><span></span><span></span></div>
  </header>

  <nav class="nav">
    <a href="#" class="active" style="width:97px">About</a>
    <a href="#" style="width:109px">Board</a>
    <a href="#" style="width:125px">Chapters</a>
    <a href="#" style="width:159px">Member Space</a>
    <a href="#" style="width:212px">Resources &amp; Knowledge</a>
    <a href="#" style="width:153px">Sponsorship</a>
    <a href="#" style="width:102px">Exhibit</a>
  </nav>

  <div class="banner" role="img" aria-label="Panoramic photo of a riverside city skyline with bridges at sunset"></div>

  <section class="box sponsors">
    <h2>Sponsors</h2>
    <div class="badge" style="left:20px;top:46px;width:56px;height:58px;background:#d8dde6"></div>
    <div class="badge" style="left:112px;top:42px;width:92px;height:68px;background:#cfe0ee;border-radius:50%"></div>
    <div class="badge" style="left:20px;top:122px;width:56px;height:56px;background:#e8d9d3"></div>
    <div class="badge" style="left:114px;top:120px;width:84px;height:62px;background:#dbe0ea"></div>
  </section>

  <section class="box login">
    <h2>Member Login</h2>
    <div class="field" style="top:50px">Username</div>
    <div class="field" style="top:91px">Password</div>
    <a href="#" class="login-btn">Login</a>
  </section>

  <section class="box connect">
    <h2>Stay Connected</h2>
    <div class="connect-icons" aria-label="Social links"><span></span><span></span><span></span><span style="background:#e8841f"></span></div>
  </section>

  <article class="welcome">
    <h1><em>Welcome to</em> Velto Canada Conference</h1>
    <p>It is a long established fact that a reader will be distracted by the readable content of a page when looking at its layout. The point of using Lorem Ipsum is that it has a more-or-less normal distribution of letters, as opposed to using 'Content here, content here', making it look like readable English.</p>
    <p>Many desktop publishing packages and web page editors now use Lorem Ipsum as their default model text, and a search for 'lorem ipsum' will uncover many web sites still in their infancy.Various versions have evolved over the years, sometimes by accident, sometimes on purpose (injected humour and the like).readable content of a page when looking at its layout. The point of using Lorem Ipsum sometimes on purpose (injected humour and the like).readable content of a page when looking at its layout. The point sometimes on purpose (injected humour and the like).</p>
  </article>

  <section class="box news">
    <h2><em>News and</em> Events</h2>
    <ul>
      <li><strong>Lorem Ipsum is simply text of</strong> <span class="desc">the also a subject matter printing</span><time>May 15 , 2012</time></li>
      <li><strong>Lorem Ipsum is simply text of</strong> <span class="desc">the also a subject matter printing</span><time>May 15 , 2012</time></li>
      <li><strong>Lorem Ipsum is simply text of</strong> <span class="desc">the also a subject matter printing</span><time>May 15 , 2012</time></li>
    </ul>
  </section>

  <section class="box regions">
    <h2>Regions</h2>
    <div class="region" style="left:25px"><h3>Mountain Pacific</h3><ul><li>Vancouver Island</li><li>Vancouver</li><li>Calgary</li></ul></div>
    <div class="region" style="left:203px"><h3>Western</h3><ul><li>Edmonton</li><li>Saskatchewan</li><li>Winnipeg</li></ul></div>
    <div class="region" style="left:366px"><h3>Central</h3><ul><li>National Capital-Ottawa</li><li>Southwestern Ontario</li><li>Montreal</li><li>Toronto</li></ul></div>
    <div class="region" style="left:560px"><h3>Atlantic</h3><ul><li>Nova Scotia</li><li>Terra-Nova, St. John’s</li><li>Prince Edward Island</li><li>Atlantic, St. John’s</li></ul></div>
  </section>
</div>

<footer class="footer">
  <p><a href="#">Home</a><span class="sep">|</span><a href="#">About</a><span class="sep">|</span><a href="#">Board</a><span class="sep">|</span><a href="#">Chapters</a><span class="sep">|</span><a href="#">Member Space</a><span class="sep">|</span><a href="#">Resources &amp; Knowledge</a><span class="sep">|</span><a href="#">Sponsorship</a><span class="sep">|</span><a href="#">Exhibit</a><span class="sep">|</span><a href="#">Member Login</a><span class="sep">|</span><a href="#">Contact Us</a></p>
  <p><a href="#">Privacy Policy</a><span class="sep">|</span><a href="#">Copyright notice</a></p>
</footer>
</body>
</html>
```